Interactive Tailored Suit and Shirt Website Needs Homepage Redesign

We need our homepage redesigned. Our current website is dated and we need a refresh. We are a Melbourne based business selling tailored suits and shirts in store and online. The homepage should be fashion forward. Our colour scheme has traditionally been black and white but would interested in new ideas.
Our current website is quillora.com.au

```html
<!DOCTYPE html>
<html lang="en">
<head>
<meta charset="utf-8">
<title>quillora — Tailored Suits &amp; Shirts</title>
<link href="https://fonts.googleapis.com/css2?family=Roboto+Condensed:wght@300;400;700&family=Comfortaa:wght@400&display=swap" rel="stylesheet">
<style>
  :root{
    --bg-dark:#262626;
    --bg-darker:#222;
    --text-light:#d6d6d6;
    --text-muted:#a9a9a9;
    --social:#4a4a4a;
    --blue:#3d8ef0;
    --orange:#f4845f;
    --green:#48bf84;
    --band:rgba(216,88,98,.88);
    --band-dark:#c84d58;
    --tab:#df5b5d;
    --white:#fff;
  }
  *{margin:0;padding:0;box-sizing:border-box}
  html,body{width:1200px;height:909px;overflow:hidden;background:var(--bg-dark)}
  body{position:relative;font-family:'Roboto Condensed',sans-serif;color:var(--text-light)}
  .narrow{display:inline-block;white-space:nowrap}

  .site-header{position:absolute;left:0;top:0;width:1200px;height:105px;background:var(--bg-dark)}
  .brand{position:absolute;left:180px;top:50px;font-family:'Comfortaa',sans-serif;font-size:27px;color:var(--white);letter-spacing:.5px}
  .main-nav{position:absolute;top:66px;left:0;font-weight:300;font-size:15px;color:var(--text-light)}
  .main-nav span{position:absolute;white-space:nowrap;transform:scaleX(.9);transform-origin:left center}
  .social{position:absolute;top:13px;left:889px;display:flex;gap:6px}
  .social span{width:28px;height:28px;border-radius:50%;background:var(--social)}
  .phone{position:absolute;top:63px;left:898px;display:flex;align-items:center;gap:6px;font-weight:300;font-size:16px;color:var(--text-light);white-space:nowrap}

  .hero{position:absolute;top:105px;left:0;width:1200px;height:613px}
  .hero-photo{position:absolute;top:0;height:613px;width:600px}
  .hero-photo.suits{left:0;background:linear-gradient(100deg,#e9e5e1 0%,#cfc9c4 40%,#8a8886 60%,#ece8e4 100%)}
  .hero-photo.shirts{left:600px;background:linear-gradient(120deg,#6f8fb5 0%,#8fb0d6 35%,#9fd9d0 55%,#c7dbe8 80%,#8b7b6f 100%)}

  .tagline{position:absolute;width:223px;height:46px;color:var(--white);font-weight:300;font-size:38px;line-height:46px;text-align:center}
  .tagline .narrow{transform:scaleX(.86);transform-origin:center}
  .tagline.design{left:486px;top:169px;background:var(--blue)}
  .tagline.fit{left:537px;top:221px;background:var(--orange)}
  .tagline.guaranteed{left:486px;top:272px;background:var(--green)}

  .category-band{position:absolute;left:293px;top:426px;width:640px;height:127px;background:var(--band)}
  .click-strip{position:absolute;top:0;width:71px;height:127px;background:var(--band-dark);display:flex;align-items:center;justify-content:center}
  .click-strip span{transform:rotate(-90deg) scaleX(.88);white-space:nowrap;font-weight:300;font-size:24px;color:var(--white)}
  .click-strip.left{left:0}
  .click-strip.right{right:0}
  .category{position:absolute;top:18px;font-weight:300;font-size:84px;line-height:94px;color:var(--white);white-space:nowrap;transform:scaleX(.82);transform-origin:left center}
  .category.suits{left:104px}
  .category.shirts{left:339px}

  .booking-tab{position:absolute;left:1161px;top:117px;width:39px;height:237px;background:var(--tab);display:flex;align-items:center;justify-content:center}
  .booking-tab span{transform:rotate(-90deg);white-space:nowrap;font-size:18px;color:var(--white)}

  .newsletter{position:absolute;top:718px;left:0;width:1200px;height:108px;background:var(--bg-dark);border-bottom:1px solid #333}
  .newsletter h2{position:absolute;top:22px;width:100%;text-align:center;font-weight:400;font-size:19px;color:var(--white)}
  .newsletter h2 .narrow{transform:scaleX(.88);transform-origin:center}
  .email-field{position:absolute;left:292px;top:62px;width:522px;height:25px;border:1px solid #444;background:var(--bg-darker);font-size:9px;color:var(--text-muted);line-height:23px;padding-left:12px}
  .submit-btn{position:absolute;left:824px;top:62px;width:75px;height:25px;border:1px solid #444;background:var(--bg-darker);font-size:11px;color:var(--white);line-height:23px;text-align:center}

  .site-footer{position:absolute;top:827px;left:0;width:1200px;height:82px;background:var(--bg-dark)}
  .footer-nav{position:absolute;top:18px;left:0;font-size:11px;color:var(--text-muted)}
  .footer-nav span{position:absolute;white-space:nowrap}
  .copyright{position:absolute;top:46px;width:100%;text-align:center;font-size:10px;color:var(--text-muted)}
</style>
</head>
<body>
  <header class="site-header">
    <div class="brand">quillora</div>
    <nav class="main-nav">
      <span style="left:396px">CUSTOMIZE YOUR OWN</span>
      <span style="left:595px">LOOK BOOK</span>
      <span style="left:720px">MY QUILLORA</span>
    </nav>
    <div class="social" aria-label="Social links">
      <span></span><span></span><span></span><span></span>
    </div>
    <div class="phone">
      <svg width="13" height="22" viewBox="0 0 13 22" aria-hidden="true">
        <rect x="0.5" y="0.5" width="12" height="21" rx="2" fill="#777"/>
        <rect x="2" y="3" width="9" height="14" fill="#333"/>
        <circle cx="6.5" cy="19" r="1" fill="#333"/>
      </svg>
      +613 9000 4821
    </div>
  </header>

  <section class="hero">
    <div class="hero-photo suits" role="img" aria-label="Man in a tailored grey suit with green tie leaning against a white wall"></div>
    <div class="hero-photo shirts" role="img" aria-label="Man in sunglasses wearing a light mint shirt against a blue sky"></div>

    <div class="tagline design"><span class="narrow">YOUR DESIGN</span></div>
    <div class="tagline fit"><span class="narrow">PERFECT FIT</span></div>
    <div class="tagline guaranteed"><span class="narrow">GUARANTEED</span></div>

    <div class="category-band">
      <div class="click-strip left"><span>CLICK HERE</span></div>
      <div class="category suits">SUITS</div>
      <div class="category shirts">SHIRTS</div>
      <div class="click-strip right"><span>CLICK HERE</span></div>
    </div>

    <div class="booking-tab"><span>APPOINTMENT BOOKING</span></div>
  </section>

  <section class="newsletter">
    <h2><span class="narrow">SIGN UP TO OUR LATEST NEWS AND EXCLUSIVE OFFERS</span></h2>
    <div class="email-field">ENTER YOUR EMAIL ID :</div>
    <div class="submit-btn">SUBMIT</div>
  </section>

  <footer class="site-footer">
    <nav class="footer-nav">
      <span style="left:270px">HOME</span>
      <span style="left:327px">CUSTOMIZE YOUR OWN</span>
      <span style="left:461px">LOOKBOOK</span>
      <span style="left:550px">ABOUT QUILLORA</span>
      <span style="left:657px">MY QUILLORA</span>
      <span style="left:764px">FAQ</span>
      <span style="left:811px">T&amp;C</span>
      <span style="left:866px">CONTACT US</span>
    </nav>
    <div class="copyright">© 2012-2013 QUILLORA. ALL RIGHT RESERVED.</div>
  </footer>
</body>
</html>
```